Business Card design for amazing new Dental Office

Please read this brief closely!

Our client is a modern new dental office/
They love their new logo.
Now it's time to create a business card for them.

It should be a two sided card:
Side one should have the logo and name and maybe a color background or design.
Side two should have all the contact information which is here:

Daniel Whitcombe, D.D.S
General and Cosmetic Dentistry
4187 W. Pinecrest Avenue
Ventura, CA 93011
(805) 912-4386
drdaniel@bluefernsmiles-example.com
www.bluefernsmiles-example.com

Feel free to arrange that info as you like and to style both sides of the card according to your creativity. This is a chance for you to show your design skills!

Client is open to font choices and is looking for a style that is amazing and premium. Colors can be selected from the logo, or any variation of those.

You will not win this contest with a less than beautiful card design so please feel free to make multiple submissions.

Logo files attached and please message me with any questions.
Thanks!

Target Market(s)

Families and Professionals seeking dental services

Industry/Entity Type

Dental

Contact Information for Business Card

Logo, style, contact info as per the brief

Font styles to use
Sans Serif

Requirements
Must have
• Client's logo and contact details as per brief
Nice to have
• Unique style reflecting high end dental clinic near the beach
Should not have
• Must not look like a template

```html
<!DOCTYPE html>
<html lang="en">
<head>
<meta charset="utf-8">
<title>Blue Fern Smiles – Business Card</title>
<link rel="stylesheet" href="https://fonts.googleapis.com/css2?family=Jost:wght@300;400&family=Lexend+Deca:wght@300;400;700&display=swap">
<style>
  :root {
    --backdrop: #3a3a3a;
    --card-white: #ffffff;
    --brand-blue: #4eb1e3;
    --link-blue: #3aa3dc;
    --name-orange: #e0a04e;
    --tagline-gold: #c9a92c;
    --logo-grey: #a9a9a9;
    --icon-grey: #9a9a9a;
    --rule-grey: #9c9c9c;
    --accent-teal: #6cc8c8;
  }
  * { margin: 0; padding: 0; box-sizing: border-box; }
  html, body { width: 1200px; height: 900px; overflow: hidden; }
  body {
    background: var(--backdrop);
    position: relative;
    font-family: "Lexend Deca", "Helvetica Neue", Arial, sans-serif;
  }
  .card { position: absolute; width: 669px; height: 382px; }

  /* Contact side */
  .card--contact { left: 272px; top: 53px; background: var(--card-white); }
  .brand-block {
    position: absolute; left: 0; top: 0; width: 333px; height: 382px;
    display: flex; flex-direction: column; align-items: center; justify-content: center;
    padding-top: 20px;
  }
  .brand-dot {
    width: 46px; height: 46px; border-radius: 50%;
    background: var(--accent-teal); margin-bottom: 26px;
  }
  .brand-name {
    font-family: "Jost", "Helvetica Neue", Arial, sans-serif;
    font-weight: 300; font-size: 30px; letter-spacing: 3px;
    text-transform: uppercase; color: var(--logo-grey); white-space: nowrap;
  }
  .divider {
    position: absolute; left: 333px; top: 42px; width: 1.5px; height: 305px;
    background: var(--rule-grey);
  }
  .details { position: absolute; left: 349px; top: 82px; }
  .doctor-name {
    font-weight: 700; font-size: 23px; color: var(--name-orange);
    letter-spacing: 0.2px; line-height: 1.1; white-space: nowrap;
  }
  .specialty { font-size: 11.5px; color: var(--tagline-gold); margin-top: 3px; }
  .contact-list { list-style: none; margin-top: 34px; }
  .contact-item {
    display: flex; align-items: center; height: 20px;
    font-size: 12.5px; color: var(--link-blue); white-space: nowrap;
  }
  .contact-item + .contact-item { margin-top: 18px; }
  .contact-item:last-child { margin-top: 12px; }
  .contact-icon { width: 16px; height: 16px; margin-right: 12px; flex: none; }

  /* Brand side */
  .card--brand { left: 272px; top: 451px; width: 670px; background: var(--brand-blue); }
  .brand-front {
    position: absolute; left: 0; top: 40px; width: 100%;
    display: flex; flex-direction: column; align-items: center;
  }
  .brand-front .brand-dot { background: #ffffff; width: 64px; height: 64px; margin-bottom: 40px; }
  .brand-front .brand-name { color: #ffffff; font-size: 34px; }
  .web-rule {
    position: absolute; left: 0; top: 240px; width: 100%; height: 7px; background: #ffffff;
  }
  .web-badge {
    position: absolute; left: 319px; top: 229px; width: 30px; height: 30px;
    border-radius: 50%; background: var(--brand-blue); border: 3px solid #ffffff;
    display: flex; align-items: center; justify-content: center;
  }
  .web-url {
    position: absolute; left: 0; top: 266px; width: 100%; text-align: center;
    font-size: 19px; font-weight: 300; color: #ffffff; letter-spacing: 0.3px;
  }
</style>
</head>
<body>
  <section class="card card--contact">
    <div class="brand-block">
      <div class="brand-dot"></div>
      <div class="brand-name">Blue Fern Smiles</div>
    </div>
    <div class="divider"></div>
    <div class="details">
      <h1 class="doctor-name">Daniel Whitcombe, D.D.S</h1>
      <p class="specialty">General and Cosmetic Dentistry</p>
      <ul class="contact-list">
        <li class="contact-item">
          <svg class="contact-icon" viewBox="0 0 16 16"><path fill="var(--icon-grey)" d="M4 1.5 6 4.5 4.8 6.2c.8 1.9 2.3 3.5 4.2 4.3L10.6 9.2l3 2-1 2.6c-.3.6-1 .9-1.7.7C6.1 13.2 2.8 9.8 1.6 5c-.2-.7.1-1.4.7-1.7Z"/></svg>
          (805) 912-4386
        </li>
        <li class="contact-item">
          <svg class="contact-icon" viewBox="0 0 16 16"><rect x="1" y="3.5" width="14" height="9" fill="var(--icon-grey)"/><path d="M1.5 4 8 9 14.5 4" fill="none" stroke="#fff" stroke-width="1.2"/></svg>
          drdaniel@bluefernsmiles-example.com
        </li>
        <li class="contact-item">
          <svg class="contact-icon" viewBox="0 0 16 16" fill="none" stroke="var(--icon-grey)" stroke-width="1.3"><circle cx="8" cy="8" r="6.5"/><ellipse cx="8" cy="8" rx="3" ry="6.5"/><path d="M1.5 8h13M2.5 4.8h11M2.5 11.2h11"/></svg>
          www.bluefernsmiles-example.com
        </li>
        <li class="contact-item">
          <svg class="contact-icon" viewBox="0 0 16 16"><path fill="var(--icon-grey)" d="M8 .5a5.3 5.3 0 0 0-5.3 5.3C2.7 9.6 8 15.5 8 15.5s5.3-5.9 5.3-9.7A5.3 5.3 0 0 0 8 .5Zm0 7.3a2 2 0 1 1 0-4 2 2 0 0 1 0 4Z"/></svg>
          4187 W. Pinecrest Avenue Ventura, CA 93011
        </li>
      </ul>
    </div>
  </section>

  <section class="card card--brand">
    <div class="brand-front">
      <div class="brand-dot"></div>
      <div class="brand-name">Blue Fern Smiles</div>
    </div>
    <div class="web-rule"></div>
    <div class="web-badge">
      <svg width="18" height="18" viewBox="0 0 16 16" fill="none" stroke="#fff" stroke-width="1.3"><circle cx="8" cy="8" r="6.5"/><ellipse cx="8" cy="8" rx="3" ry="6.5"/><path d="M1.5 8h13M2.5 4.8h11M2.5 11.2h11"/></svg>
    </div>
    <p class="web-url">www.bluefernsmiles-example.com</p>
  </section>
</body>
</html>
```